Process Flow Chart for Real Estate Agency

We need a visual flow chart of the process of selling a home for our Real Estate Agency. This visual will be provided to all new staff to explain the process and also to potential clients to explain how detailed the process is. It needs to show each step as detailed in the attached word doc and use icons and arrows to show the direction of flow.

Target Market(s)

Staff & Potential Clients

Industry/Entity Type

Real Estate

Font styles to use
Sans Serif

Colors

Designer to choose colors to be used in the design.

Requirements
Must have
• Easy to read, lots of icons, colour coded with Agent in one colour, Admin in another (some tasks are either/or so not sure what to colour those ones.)
Nice to have
• Include one of the two attached logos

```html
<!DOCTYPE html>
<html lang="en">
<head>
<meta charset="utf-8">
<title>HarborLane Realty – Selling Process Flow</title>
<link rel="stylesheet" href="https://fonts.googleapis.com/css2?family=Open+Sans:wght@400;600;700;800&display=swap">
<style>
  :root {
    --agent-blue: #1b8ad3;
    --admin-orange: #f37021;
    --shared-yellow: #f6be17;
    --ink: #1f1f22;
    --text: #232326;
    --paper: #ffffff;
    --connector: #2b2b2e;
    --skyline: #eef0f3;
  }
  html, body { margin: 0; padding: 0; overflow: hidden; background: var(--paper); }
  .canvas {
    position: relative;
    width: 1200px;
    height: 3056px;
    overflow: hidden;
    background: var(--paper);
    font-family: "Open Sans", Arial, sans-serif;
    color: var(--text);
  }
  .corner, .connectors, .skyline { position: absolute; }
  .corner-top-left { left: 0; top: 0; }
  .corner-top-right { right: 0; top: 0; }
  .corner-bottom { left: 0; bottom: 0; }
  .skyline {
    left: 0; bottom: 20px; width: 1200px; height: 300px;
    background: linear-gradient(to top, var(--skyline), rgba(238,240,243,0));
  }

  .brand {
    position: absolute;
    left: 440px; top: 176px;
    width: 680px;
    display: flex; align-items: center; gap: 20px;
  }
  .brand-mark {
    width: 40px; height: 40px; border-radius: 50%;
    background: var(--admin-orange);
    flex: none;
  }
  .brand-name {
    margin: 0;
    font-weight: 800;
    font-size: 66px;
    line-height: 1;
    letter-spacing: -1px;
    color: var(--ink);
    white-space: nowrap;
  }

  .task-rule {
    position: absolute; left: 230px; top: 344px;
    width: 970px; height: 6px; background: var(--ink);
  }
  .task-tab {
    position: absolute; left: 520px; top: 328px;
    width: 164px; height: 74px;
    background: var(--ink);
    border-radius: 0 0 40px 40px;
    color: #fff;
    font-weight: 800; font-size: 36px; letter-spacing: 2px;
    text-align: center; line-height: 62px;
  }
  .task-tab svg { position: absolute; left: 68px; top: 54px; }

  .step-box {
    position: absolute;
    height: 80px;
    box-sizing: border-box;
    border: 2px dashed var(--agent-blue);
    background: var(--paper);
    display: flex; align-items: center; justify-content: center;
    text-align: center;
    padding: 0 40px;
    font-weight: 600; font-size: 24px; line-height: 1.25;
  }
  .step-box.icon-left { left: 198px; width: 905px; padding-left: 60px; }
  .step-box.icon-right { left: 102px; width: 918px; padding-right: 70px; }
  .step-box.admin { border-color: var(--admin-orange); }
  .step-box.shared { border-color: var(--shared-yellow); }

  .step-icon {
    position: absolute;
    width: 110px; height: 110px;
    border-radius: 50%;
    background: var(--agent-blue);
    display: flex; align-items: center; justify-content: center;
    box-shadow: 0 0 0 4px #fff;
  }
  .step-icon.left { left: 98px; }
  .step-icon.right { left: 997px; }
  .step-icon.admin { background: var(--admin-orange); }
  .step-icon.shared { background: var(--shared-yellow); }
  .step-icon svg { width: 60px; height: 60px; }
  .glyph { fill: none; stroke: #fff; stroke-width: 3; stroke-linecap: round; stroke-linejoin: round; }
  .glyph-fill { fill: #fff; }
</style>
</head>
<body>
<div class="canvas">

  <svg class="corner corner-top-left" width="420" height="340" viewBox="0 0 420 340" aria-hidden="true">
    <polygon points="0,0 130,0 0,110" fill="#ffb21c"/>
    <polygon points="130,0 230,0 0,195 0,110" fill="#f37021"/>
    <polygon points="230,0 300,0 0,255 0,195" fill="#e0541b"/>
    <polygon points="300,0 420,0 420,20 60,340 0,340 0,255" fill="#1f1f22"/>
  </svg>
  <svg class="corner corner-top-right" width="120" height="100" viewBox="0 0 120 100" aria-hidden="true">
    <polygon points="0,0 120,0 120,100" fill="#1b8ad3"/>
  </svg>

  <div class="brand">
    <span class="brand-mark" aria-hidden="true"></span>
    <p class="brand-name">HarborLane Realty</p>
  </div>

  <div class="task-rule"></div>
  <div class="task-tab">TASK
    <svg width="28" height="14" viewBox="0 0 28 14" aria-hidden="true"><polyline points="2,2 14,12 26,2" fill="none" stroke="#f37021" stroke-width="3"/></svg>
  </div>

  <div class="skyline" role="img" aria-label="Faint city skyline silhouette"></div>

  <svg class="connectors" width="1200" height="3056" viewBox="0 0 1200 3056" aria-hidden="true"
       style="left:0;top:0" fill="none" stroke="var(--connector)" stroke-width="2" stroke-dasharray="7 6">
    <path d="M1103 515 H1135 V635 H1114"/>
    <path d="M102 635 H68 V755 H90"/>
    <path d="M1103 755 H1135 V875 H1114"/>
    <path d="M102 875 H68 V995 H90"/>
    <path d="M1103 995 H1135 V1115 H1114"/>
    <path d="M102 1115 H68 V1235 H90"/>
    <path d="M1103 1235 H1135 V1355 H1114"/>
    <path d="M102 1355 H68 V1475 H90"/>
    <path d="M1103 1475 H1135 V1595 H1114"/>
    <path d="M102 1595 H68 V1715 H90"/>
    <path d="M1103 1715 H1135 V1835 H1114"/>
    <path d="M102 1835 H68 V1955 H90"/>
    <path d="M1103 1955 H1135 V2075 H1114"/>
    <path d="M102 2075 H68 V2195 H90"/>
    <path d="M1103 2195 H1135 V2315 H1114"/>
    <path d="M102 2315 H68 V2435 H90"/>
    <path d="M1103 2435 H1135 V2555 H1114"/>
    <path d="M102 2555 H68 V2675 H90"/>
    <path d="M1103 2675 H1135 V2795 H1114"/>
    <g fill="var(--connector)" stroke="none">
      <polygon points="1108,635 1118,629 1118,641"/><polygon points="96,755 86,749 86,761"/>
      <polygon points="1108,875 1118,869 1118,881"/><polygon points="96,995 86,989 86,1001"/>
      <polygon points="1108,1115 1118,1109 1118,1121"/><polygon points="96,1235 86,1229 86,1241"/>
      <polygon points="1108,1355 1118,1349 1118,1361"/><polygon points="96,1475 86,1469 86,1481"/>
      <polygon points="1108,1595 1118,1589 1118,1601"/><polygon points="96,1715 86,1709 86,1721"/>
      <polygon points="1108,1835 1118,1829 1118,1841"/><polygon points="96,1955 86,1949 86,1961"/>
      <polygon points="1108,2075 1118,2069 1118,2081"/><polygon points="96,2195 86,2189 86,2201"/>
      <polygon points="1108,2315 1118,2309 1118,2321"/><polygon points="96,2435 86,2429 86,2441"/>
      <polygon points="1108,2555 1118,2549 1118,2561"/><polygon points="96,2675 86,2669 86,2681"/>
      <polygon points="1108,2795 1118,2789 1118,2801"/>
    </g>
  </svg>

  <svg width="0" height="0" style="position:absolute" aria-hidden="true">
    <defs>
      <symbol id="i-phone" viewBox="0 0 48 48"><path class="glyph" d="M14 6 L20 6 L23 15 L18 19 Q22 28 29 31 L33 26 L42 29 L42 35 Q40 42 33 41 Q12 36 7 15 Q7 7 14 6Z"/></symbol>
      <symbol id="i-meeting" viewBox="0 0 48 48"><g class="glyph"><rect x="8" y="26" width="32" height="6" rx="1"/><line x1="14" y1="32" x2="14" y2="42"/><line x1="34" y1="32" x2="34" y2="42"/></g><g class="glyph-fill"><circle cx="12" cy="14" r="4"/><circle cx="24" cy="11" r="4"/><circle cx="36" cy="14" r="4"/></g></symbol>
      <symbol id="i-contact" viewBox="0 0 48 48"><g class="glyph"><rect x="6" y="12" width="36" height="26" rx="2"/><polyline points="6,14 24,28 42,14"/></g></symbol>
      <symbol id="i-calendar" viewBox="0 0 48 48"><g class="glyph"><rect x="7" y="10" width="34" height="32" rx="2"/><line x1="7" y1="18" x2="41" y2="18"/><line x1="15" y1="6" x2="15" y2="13"/><line x1="33" y1="6" x2="33" y2="13"/></g><g class="glyph-fill"><rect x="12" y="23" width="5" height="4"/><rect x="21.5" y="23" width="5" height="4"/><rect x="31" y="23" width="5" height="4"/><rect x="12" y="32" width="5" height="4"/><rect x="21.5" y="32" width="5" height="4"/></g></symbol>
      <symbol id="i-sms" viewBox="0 0 48 48"><g class="glyph"><path d="M6 10 H42 V32 H20 L11 40 V32 H6Z"/><line x1="13" y1="18" x2="35" y2="18"/><line x1="13" y1="25" x2="29" y2="25"/></g></symbol>
      <symbol id="i-doc" viewBox="0 0 48 48"><g class="glyph"><path d="M12 5 H30 L38 13 V43 H12Z"/><polyline points="30,5 30,13 38,13"/><line x1="17" y1="21" x2="33" y2="21"/><line x1="17" y1="28" x2="33" y2="28"/><line x1="17" y1="35" x2="28" y2="35"/></g></symbol>
      <symbol id="i-house" viewBox="0 0 48 48"><g class="glyph"><polyline points="5,24 24,8 43,24"/><path d="M11 20 V42 H37 V20"/><rect x="20" y="28" width="8" height="14"/></g></symbol>
      <symbol id="i-kit" viewBox="0 0 48 48"><g class="glyph"><rect x="8" y="12" width="26" height="32" rx="1"/><path d="M14 12 V6 H40 V38 H34"/><line x1="13" y1="20" x2="29" y2="20"/><line x1="13" y1="27" x2="29" y2="27"/><line x1="13" y1="34" x2="24" y2="34"/></g></symbol>
      <symbol id="i-send" viewBox="0 0 48 48"><g class="glyph"><polygon points="4,22 44,6 34,42 24,28"/><line x1="24" y1="28" x2="44" y2="6"/><polyline points="24,28 22,40 28,33"/></g></symbol>
      <symbol id="i-chart" viewBox="0 0 48 48"><g class="glyph"><path d="M10 4 H38 V44 H10Z"/><line x1="17" y1="38" x2="17" y2="30"/><line x1="24" y1="38" x2="24" y2="24"/><line x1="31" y1="38" x2="31" y2="18"/><line x1="17" y1="11" x2="31" y2="11"/></g></symbol>
      <symbol id="i-deal" viewBox="0 0 48 48"><g class="glyph"><polyline points="4,18 14,12 24,18 34,12 44,18"/><path d="M12 22 L22 32 Q25 35 28 32 L36 24"/><line x1="18" y1="28" x2="24" y2="22"/></g></symbol>
      <symbol id="i-house-dollar" viewBox="0 0 48 48"><g class="glyph"><polyline points="5,24 24,8 43,24"/><path d="M11 20 V42 H37 V20"/><path d="M28 26 Q24 23 21 25 Q19 28 24 30 Q29 32 27 35 Q24 37 20 34"/><line x1="24" y1="22" x2="24" y2="38"/></g></symbol>
      <symbol id="i-confirm" viewBox="0 0 48 48"><g class="glyph"><rect x="9" y="8" width="30" height="36" rx="2"/><rect x="17" y="4" width="14" height="7" rx="1"/><polyline points="16,26 22,32 33,20"/></g></symbol>
      <symbol id="i-visit" viewBox="0 0 48 48"><g class="glyph"><path d="M4 28 L14 20 L22 24 L30 18 L44 28"/><path d="M14 20 L24 34 Q27 37 30 34 L34 30"/></g></symbol>
      <symbol id="i-gift" viewBox="0 0 48 48"><g class="glyph"><rect x="7" y="18" width="34" height="8"/><rect x="10" y="26" width="28" height="17"/><line x1="24" y1="18" x2="24" y2="43"/><path d="M24 18 Q16 6 12 12 Q10 17 24 18 Q38 17 36 12 Q32 6 24 18"/></g></symbol>
      <symbol id="i-list" viewBox="0 0 48 48"><g class="glyph"><rect x="9" y="8" width="28" height="36" rx="2"/><line x1="15" y1="17" x2="31" y2="17"/><line x1="15" y1="24" x2="31" y2="24"/><line x1="15" y1="31" x2="24" y2="31"/></g><circle class="glyph-fill" cx="36" cy="37" r="8"/><polyline points="32,37 35,40 40,34" fill="none" stroke="#1b8ad3" stroke-width="2.5"/></symbol>
      <symbol id="i-sign" viewBox="0 0 48 48"><g class="glyph"><path d="M30 6 L40 16 L18 38 L6 42 L10 30Z"/><line x1="26" y1="10" x2="36" y2="20"/><line x1="24" y1="42" x2="42" y2="42"/></g></symbol>
      <symbol id="i-sale" viewBox="0 0 48 48"><g class="glyph"><rect x="5" y="12" width="38" height="20" rx="1"/><line x1="12" y1="32" x2="12" y2="44"/><line x1="36" y1="32" x2="36" y2="44"/><line x1="12" y1="12" x2="12" y2="5"/><line x1="36" y1="12" x2="36" y2="5"/></g><text x="24" y="27" text-anchor="middle" font-family="Open Sans, sans-serif" font-weight="800" font-size="11" fill="#fff">SALE</text></symbol>
      <symbol id="i-checkbox" viewBox="0 0 48 48"><g class="glyph"><rect x="7" y="10" width="30" height="30" rx="2"/><polyline points="14,24 22,32 42,8"/></g></symbol>
      <symbol id="i-mail" viewBox="0 0 48 48"><g class="glyph"><polyline points="6,20 24,6 42,20"/><rect x="6" y="20" width="36" height="22"/><polyline points="6,20 24,33 42,20"/><line x1="16" y1="14" x2="32" y2="14"/></g></symbol>
    </defs>
  </svg>

  <div class="step-box icon-left agent" style="top:475px">Agent calls potential client to arrange a time to meet and obtain details about the property</div>
  <div class="step-icon left agent" style="top:460px"><svg><use href="#i-phone"/></svg></div>

  <div class="step-box icon-right agent" style="top:595px">Agent ensures all decision makers will be present at meeting</div>
  <div class="step-icon right agent" style="top:580px"><svg><use href="#i-meeting"/></svg></div>

  <div class="step-box icon-left agent" style="top:715px">Agent adds vendors contact details on phone</div>
  <div class="step-icon left agent" style="top:700px"><svg><use href="#i-contact"/></svg></div>

  <div class="step-box icon-right agent" style="top:835px">Agent adds appointment to personal calendar</div>
  <div class="step-icon right agent" style="top:820px"><svg><use href="#i-calendar"/></svg></div>

  <div class="step-box icon-left agent" style="top:955px">Agent sends SMS to potential client to thank them for the opportunity</div>
  <div class="step-icon left agent" style="top:940px"><svg><use href="#i-sms"/></svg></div>

  <div class="step-box icon-right shared" style="top:1075px">Agent/Admin orders ARE from Brantwick's</div>
  <div class="step-icon right shared" style="top:1060px"><svg><use href="#i-doc"/></svg></div>

  <div class="step-box icon-left agent" style="top:1195px">Agent completes a TMP to provide to Admin for Prelisting kit prep</div>
  <div class="step-icon left agent" style="top:1180px"><svg><use href="#i-house"/></svg></div>

  <div class="step-box icon-right admin" style="top:1315px">Admin prepares pre-listing kit with questionnaire, sample brochure &amp; cover letter, property magazine, agent profile booklet</div>
  <div class="step-icon right admin" style="top:1300px"><svg><use href="#i-kit"/></svg></div>

  <div class="step-box icon-left shared" style="top:1435px">Admin/Agent delivers pre-listing kit (preferably within the hour) &amp; SMS potential vendor</div>
  <div class="step-icon left shared" style="top:1420px"><svg><use href="#i-send"/></svg></div>

  <div class="step-box icon-right admin" style="top:1555px">Admin/Agent to research &amp; prints comparable Sales reports</div>
  <div class="step-icon right admin" style="top:1540px"><svg><use href="#i-chart"/></svg></div>

  <div class="step-box icon-left admin" style="top:1666px;height:98px">Admin prepares TMP with Marketing Costs Selection booklet, Service Offering Selection booklet, Sales Agency Agreement &amp; Benefits Form, ARE</div>
  <div class="step-icon left admin" style="top:1660px"><svg><use href="#i-deal"/></svg></div>

  <div class="step-box icon-right admin" style="top:1795px">Admin enters potential Vendor into CRM &amp; set “Appraisal” Track</div>
  <div class="step-icon right admin" style="top:1780px"><svg><use href="#i-house-dollar"/></svg></div>

  <div class="step-box icon-left agent" style="top:1915px">Agent confirms appraisal on the morning of the appointment with an SMS</div>
  <div class="step-icon left agent" style="top:1900px"><svg><use href="#i-confirm"/></svg></div>

  <div class="step-box icon-right agent" style="top:2035px">Agent meets with potential Vendor and completes the appraisal</div>
  <div class="step-icon right agent" style="top:2020px"><svg><use href="#i-visit"/></svg></div>

  <div class="step-box icon-left admin" style="top:2155px">Admin prepares written appraisal report hand-deliver with coffee vouchers &amp;/or gift</div>
  <div class="step-icon left admin" style="top:2140px"><svg><use href="#i-gift"/></svg></div>

  <div class="step-box icon-right agent" style="top:2275px">Agent hand-delivers report with coffee voucher or Marlowe's chocolates</div>
  <div class="step-icon right agent" style="top:2260px"><svg><use href="#i-list"/></svg></div>

  <div class="step-box icon-left agent" style="top:2395px">Agent receives confirmation from vendor to proceed with listing &amp; arranges signing of Residential Sales Agency Agreement</div>
  <div class="step-icon left agent" style="top:2380px"><svg><use href="#i-sign"/></svg></div>

  <div class="step-box icon-right admin" style="top:2515px">Admin checks Residential Sales Agency &amp; enters as Listing into CRM</div>
  <div class="step-icon right admin" style="top:2500px"><svg><use href="#i-sale"/></svg></div>

  <div class="step-box icon-left admin" style="top:2635px">Admin completes the "New Listing Checklist" and prepares black folder</div>
  <div class="step-icon left admin" style="top:2620px"><svg><use href="#i-checkbox"/></svg></div>

  <div class="step-box icon-right admin" style="top:2755px">Admin checks for Vendor email addresses &amp; if required call or SMS client to obtain</div>
  <div class="step-icon right admin" style="top:2740px"><svg><use href="#i-mail"/></svg></div>

  <svg class="corner corner-bottom" width="1200" height="140" viewBox="0 0 1200 140" aria-hidden="true">
    <polygon points="0,120 1200,120 1200,140 0,140" fill="#1f1f22"/>
    <polygon points="0,70 60,120 0,120" fill="#1f1f22"/>
    <polygon points="1200,0 1200,40 1110,120 1070,120" fill="#1f1f22"/>
    <polygon points="1200,40 1200,85 1160,120 1110,120" fill="#f37021"/>
    <polygon points="1200,85 1200,120 1160,120" fill="#ffb21c"/>
  </svg>
</div>
</body>
</html>
```